Realtor branding business card

modern, simple and self branding. Broker office logo needs to be used but not emphasized. Looking to brand myself

Target Market(s)

buyers, sellers and investors

Industry/Entity Type

Realtor

Contact Information for Business Card

Sample of my current business card on file

Requirements
Must have
• my website - emilioverdaskt.com
• Realtor logo
• Fair housing logo
Nice to have
• Colors from office logo but not a must
Should not have
• Do not want headshot

```html
<!DOCTYPE html>
<html lang="en">
<head>
<meta charset="utf-8">
<title>Emilio Verdask – Realtor Business Card</title>
<link href="https://fonts.googleapis.com/css2?family=Abel&family=Oswald:wght@600&display=swap" rel="stylesheet">
<style>
  :root {
    --navy: #0b1c34;
    --red: #a52324;
    --white: #ffffff;
    --backdrop: #dfe0e3;
  }
  * { box-sizing: border-box; margin: 0; padding: 0; }
  html, body { width: 1200px; height: 800px; overflow: hidden; }
  body { background: var(--backdrop); position: relative; }

  .card {
    position: absolute;
    width: 496px;
    height: 320px;
    overflow: hidden;
  }
  .card--front { left: 331px; top: 38px; }
  .card--back { left: 329px; top: 386px; background: var(--navy); }

  .card__shape { position: absolute; inset: 0; }

  .brand {
    position: absolute;
    left: 30px;
    top: 24px;
    font-family: "Oswald", sans-serif;
    font-weight: 600;
    color: var(--navy);
    line-height: 1;
  }
  .brand__name { display: block; font-size: 36px; letter-spacing: -0.3px; }
  .brand__role {
    display: block;
    margin-top: 6px;
    font-family: "Abel", sans-serif;
    font-weight: 400;
    font-size: 12px;
    letter-spacing: 1.4px;
    text-transform: uppercase;
    color: var(--navy);
  }
  .brand__role .brand__broker { color: var(--red); }

  .contact { position: absolute; left: 29px; top: 136px; list-style: none; }
  .contact__item {
    display: flex;
    align-items: center;
    gap: 9px;
    height: 30px;
    margin-bottom: 24px;
    font-family: "Abel", sans-serif;
    font-size: 11.5px;
    line-height: 14.5px;
    color: var(--navy);
  }
  .contact__icon {
    width: 28px; height: 28px; border-radius: 50%;
    background: var(--red);
    display: flex; align-items: center; justify-content: center;
    flex: none;
  }
  .contact__label { color: var(--red); }

  .back-name {
    position: absolute;
    left: 0; right: 0; top: 112px;
    text-align: center;
    font-family: "Oswald", sans-serif;
    font-weight: 600;
    font-size: 56px;
    line-height: 1;
    color: var(--red);
  }

  .badges {
    position: absolute;
    left: 0; right: 0; bottom: 26px;
    display: flex;
    justify-content: center;
    gap: 14px;
  }
  .badge {
    width: 26px; height: 26px;
    background: var(--white);
  }
</style>
</head>
<body>

<section class="card card--front">
  <svg class="card__shape" viewBox="0 0 496 320" width="496" height="320" aria-hidden="true">
    <rect width="496" height="320" fill="var(--navy)"/>
    <path d="M300 157 L390.7 157 C394 190 388 270 368 320 L250 320 Z" fill="var(--red)"/>
    <path d="M390.7 157 C394 190 388 270 368 320" fill="none" stroke="var(--white)" stroke-width="3"/>
    <path d="M0 0 L323 0 C368 50 396 130 392 200 C387 255 330 302 267 320 L0 320 Z" fill="var(--white)"/>
  </svg>

  <div class="brand">
    <span class="brand__name">Emilio Verdask</span>
    <span class="brand__role">Realtor · <span class="brand__broker">Brightgate Realty Group</span></span>
  </div>

  <ul class="contact">
    <li class="contact__item">
      <span class="contact__icon">
        <svg width="14" height="14" viewBox="0 0 24 24" aria-hidden="true"><path fill="#fff" d="M6.6 10.8a15.1 15.1 0 0 0 6.6 6.6l2.2-2.2a1 1 0 0 1 1-.25 11.4 11.4 0 0 0 3.6.57 1 1 0 0 1 1 1V20a1 1 0 0 1-1 1A17 17 0 0 1 3 4a1 1 0 0 1 1-1h3.5a1 1 0 0 1 1 1c0 1.25.2 2.45.57 3.57a1 1 0 0 1-.25 1z"/></svg>
      </span>
      <span><span class="contact__label">Cell:</span> 407.555.0148<br><span class="contact__label">Office:</span> 407.555.0190</span>
    </li>
    <li class="contact__item">
      <span class="contact__icon">
        <svg width="14" height="14" viewBox="0 0 24 24" aria-hidden="true"><path fill="#fff" d="M12 2a7 7 0 0 0-7 7c0 5.2 7 13 7 13s7-7.8 7-13a7 7 0 0 0-7-7zm0 9.5A2.5 2.5 0 1 1 12 6.5a2.5 2.5 0 0 1 0 5z"/></svg>
      </span>
      <span><span class="contact__label">480</span> Lakeview Crest Dr.<br><span class="contact__label">Winter Park</span>, FL 32789</span>
    </li>
    <li class="contact__item">
      <span class="contact__icon">
        <svg width="15" height="15" viewBox="0 0 24 24" aria-hidden="true" fill="none" stroke="#fff" stroke-width="1.6"><circle cx="12" cy="12" r="9"/><path d="M3 12h18M12 3c3 3.2 3 14.8 0 18M12 3c-3 3.2-3 14.8 0 18M4.5 7.5h15M4.5 16.5h15"/></svg>
      </span>
      <span><span class="contact__label">WWW.</span>emilioverdaskt<span class="contact__label">.com</span><br><span class="contact__label">WWW.</span>brightgatefl<span class="contact__label">.com</span></span>
    </li>
  </ul>
</section>

<section class="card card--back">
  <p class="back-name">Emilio Verdask</p>
  <div class="badges">
    <span class="badge" role="img" aria-label="Realtor membership mark"></span>
    <span class="badge" role="img" aria-label="Equal housing opportunity mark"></span>
  </div>
</section>

</body>
</html>
```